Business Card Design Project

We're an orthopaedic office, and our colors are blue white and balck. Dealing with physicians and healthcare execs, I'd like this card to have a classy, yet overpowering wow factor.

Here are a couple of cards I like that are close to what I'm looking for:
http://www.pixelbazaro.com/design/392047
http://www.pixelbazaro.com/design/286390

Industry/Entity Type

Healthcare

```html
<!DOCTYPE html>
<html lang="en">
<head>
<meta charset="utf-8">
<title>Riverbend Orthopaedic &amp; Sports Medicine Center – Business Cards</title>
<link rel="stylesheet" href="https://fonts.googleapis.com/css2?family=Questrial&display=swap">
<style>
  :root {
    --backdrop: #1c1c1e;
    --card-blue: #2f34b8;
    --card-blue-deep: #262a9c;
    --ink-white: #ffffff;
    --ink-soft: rgba(255,255,255,0.82);
    --rule: rgba(255,255,255,0.55);
  }
  * { margin: 0; padding: 0; box-sizing: border-box; }
  html, body {
    width: 1200px; height: 900px; overflow: hidden;
    background: var(--backdrop);
    font-family: "Questrial", "Century Gothic", sans-serif;
    color: var(--ink-white);
  }
  .canvas {
    position: relative; width: 1200px; height: 900px;
    display: flex; flex-direction: column; align-items: center; justify-content: center; gap: 24px;
  }
  .card {
    position: relative; width: 700px; height: 400px;
    background: linear-gradient(135deg, var(--card-blue) 0%, var(--card-blue-deep) 100%);
    box-shadow: 0 18px 40px rgba(0,0,0,0.55);
    overflow: hidden;
  }

  /* Contact side */
  .card--contact { display: flex; align-items: center; padding: 0 60px; }
  .contact-brand { width: 280px; display: flex; align-items: center; gap: 14px; }
  .brand-square { width: 46px; height: 46px; background: var(--ink-white); flex: none; }
  .brand-name { font-size: 22px; line-height: 1.15; text-transform: uppercase; letter-spacing: 0.5px; }
  .brand-name small { display: block; font-size: 13px; letter-spacing: 0.3px; text-transform: none; }
  .contact-rule { width: 1px; height: 170px; background: var(--rule); margin: 0 26px 0 20px; }
  .contact-details { display: flex; flex-direction: column; gap: 8px; }
  .person-name { font-size: 20px; letter-spacing: 1px; text-transform: uppercase; }
  .person-title { font-size: 13px; color: var(--ink-soft); margin-top: -6px; margin-bottom: 6px; }
  .contact-line { display: flex; align-items: center; gap: 10px; font-size: 13.5px; color: var(--ink-soft); }
  .contact-icon { width: 16px; height: 16px; flex: none; }

  /* Front side */
  .card--front { display: flex; align-items: center; padding: 0 70px; gap: 28px; }
  .front-square { width: 110px; height: 110px; background: var(--ink-white); flex: none; }
  .front-name { text-transform: uppercase; line-height: 1; }
  .front-name .line-main { display: block; font-size: 58px; letter-spacing: 1px; }
  .front-name .line-sub { display: block; font-size: 27px; letter-spacing: 0.5px; margin-top: 6px; }
  .front-name .line-tail { display: block; font-size: 22px; text-transform: none; text-align: right; margin-top: 4px; }
</style>
</head>
<body>
<main class="canvas">

  <section class="card card--contact" aria-label="Business card, contact side">
    <div class="contact-brand">
      <span class="brand-square" aria-hidden="true"></span>
      <p class="brand-name">Riverbend<br>Orthopaedic &amp; Sports<small>Medicine Center</small></p>
    </div>
    <span class="contact-rule" aria-hidden="true"></span>
    <div class="contact-details">
      <p class="person-name">Dana Whitfield</p>
      <p class="person-title">CEO</p>
      <p class="contact-line">
        <svg class="contact-icon" viewBox="0 0 16 16" aria-hidden="true"><rect x="0.5" y="0.5" width="15" height="15" rx="3" fill="none" stroke="#fff"/><path d="M5 4c1 0 1.5 2 1 2.5l-.7.7c.6 1.3 1.3 2 2.5 2.5l.7-.7c.5-.5 2.5 0 2.5 1 0 1-1 1.5-1.5 1.5C6.5 11.5 4.5 9.5 4 6 4 5 4.5 4 5 4z" fill="#fff"/></svg>
        (555) 010-4827
      </p>
      <p class="contact-line">
        <svg class="contact-icon" viewBox="0 0 16 16" aria-hidden="true"><rect x="0.5" y="0.5" width="15" height="15" rx="3" fill="none" stroke="#fff"/><rect x="3.5" y="5" width="9" height="6" fill="none" stroke="#fff"/><path d="M3.5 5l4.5 3.5L12.5 5" fill="none" stroke="#fff"/></svg>
        dwhitfield@riverbendortho.com
      </p>
      <p class="contact-line">
        <svg class="contact-icon" viewBox="0 0 16 16" aria-hidden="true"><rect x="0.5" y="0.5" width="15" height="15" rx="3" fill="none" stroke="#fff"/><circle cx="8" cy="8" r="4.5" fill="none" stroke="#fff"/><path d="M3.5 8h9M8 3.5c-2 2.5-2 6.5 0 9M8 3.5c2 2.5 2 6.5 0 9" fill="none" stroke="#fff" stroke-width="0.8"/></svg>
        www.riverbendortho.com
      </p>
      <p class="contact-line">
        <svg class="contact-icon" viewBox="0 0 16 16" aria-hidden="true"><rect x="0.5" y="0.5" width="15" height="15" rx="3" fill="none" stroke="#fff"/><path d="M8 13s-3.5-3.6-3.5-6A3.5 3.5 0 0 1 11.5 7C11.5 9.4 8 13 8 13z" fill="#fff"/><circle cx="8" cy="7" r="1.3" fill="#2f34b8"/></svg>
        1208 Cedar Ridge Rd, Fairview, LA 70012
      </p>
    </div>
  </section>

  <section class="card card--front" aria-label="Business card, front side">
    <span class="front-square" aria-hidden="true"></span>
    <h1 class="front-name">
      <span class="line-main">Riverbend</span>
      <span class="line-sub">Orthopaedic &amp; Sports</span>
      <span class="line-tail">Medicine Center</span>
    </h1>
  </section>

</main>
</body>
</html>
```